Indie Filmmakers Need Awesome Documentary Poster

BRAVELL Productions, an independent film/video production company needs a poster to publicize its upcoming documentary entitled, "Copper Vigil". Copper Vigil is a film about the underground world of guerilla film collectors and preservationists. These people are not usually associated with an archive nor do they really make any money off their work. They collect, share and preserve films using money from their "day jobs" to save them for future generations. They are fighting the goliaths of unfair copyright laws and studio negligence in order to preserve what is often the last print of an old film for future generations. One of our subjects actually dumpster dives for film and restores it. Another actually won a special academy award for his work during the making of our film.

We are looking for one of two poster designs (we can't decide which to go with yet).
But first, a bit about the overall feel and look we are hoping for. Because these subjects are really heroes to us, we would like the tone of the poster to reflect that so we're not going for laughs here at all.

Design 1 (We call it the Pizza Design) is based on the visual of the last piece of pizza on an otherwise empty cardboard circle except instead of a slice of pizza, it should be a section of a film reel (cut in the classic triangle pizza shape). Title "Copper Vigil" must be prominently featured as well as the tagline "Hurry! They're saving you a piece!"

Design 2 (We call it Dumpster Victory Design) is set up as follows: In the foreground is a dumpster with a figure standing triumphantly in it. The figure’s hand is raised above his head in a pose of victory clutching a film reel from which strips of film cascade down around his shoulders. We are including a picture of the face we'd like on that figure. He has wild hair and quite a beard. The dumpster can be filled with unspooled film as well. We are including a screencap of a statue that gives an idea of the way we’d like the film reel and strips to cascade around the figure. In the background, we’d like see a studio soundstage door or gates to a studio implying our guy is outside the studio diving in their dumpster. The dumpster could even have “studio trash” stenciled on it. Peeking out of the dumpster could also be iconic items like the sled from Harbor Lantern, Valdomar’s hat, and again, the title “Copper Vigil” should figure prominently in the design as well as the tagline “Stopping at nothing to save your film history!”

Design 3 (Your design) Is whatever you as an artist thinks will best communicate the sense of urgency, subject matter (guerilla film preservation and collectors as the heroic keepers of lost film, etc.)

Please note the tagline changes depending on which design you are creating.

We are attaching some photos that you could use to help visualize the design.

Specs:
• Title should be predominantly featured: “Copper Vigil”
• Above title should read: “BRAVELL Productions Presents:”
• Tagline should be included (see above as tagline differs depending on design)
• Final product should be 27 x 40 inches (portrait style)
• File should be in editable layered photoshop file, 300 dpi
• Editable credit block should be at bottom of poster, please include (as part of credit block) Written, Produced, Directed and Edited by Meredith L. Dunbar & Owen R. Feldmann
• Under credit block predominant text should read: www.coppervigilmovie.example

Target Market(s)

Movie goers, distribution executives at studios, film festival attendees. This needs to look like a poster you would find in an American movie house. Thanks!

Industry/Entity Type

Hair

Font styles to use
Sans Serif

Requirements
Must have
• Must haves are listed in project description above.
Nice to have
• More of the design #2 concepts of the guy in the dumpster triumphantly holding the film reel above his head in victory.
Should not have
• NOTE: We've been getting a lot of flat kind of movie reel ideas. We need it to appear more three dimensional like a pizza in a pizza box with the ghost of the reel on the cardboard and a hand picking up the last slice of the reel (maybe with some film strips hanging from the reel and some snippets in the box like it's the last piece of pizza.) We are attaching a mockup picture for your inspiration (see file called "Pizza Idea Mockup" below please). Do not use this photo for the poster. Thanks so much (and please, we are hoping someone is working on the dumpster idea too).

```html
<!DOCTYPE html>
<html lang="en">
<head>
<meta charset="utf-8">
<title>Copper Vigil — Poster</title>
<link rel="stylesheet" href="https://fonts.googleapis.com/css2?family=Antonio:wght@400;500;600;700&display=swap">
<style>
  :root {
    --backdrop: #e9e8e6;
    --paper: #ffffff;
    --ink: #121212;
    --accent: #d3202a;
    --muted: #3a3a3a;
    --photo-light: #d9d9d9;
    --photo-dark: #7c7c7c;
  }
  * { margin: 0; padding: 0; box-sizing: border-box; }
  html, body {
    width: 1200px; height: 1148px; overflow: hidden;
    background: var(--backdrop);
    font-family: "Antonio", "Arial Narrow", sans-serif;
    color: var(--ink);
  }
  .canvas {
    width: 1200px; height: 1148px;
    display: flex; align-items: center; justify-content: center;
  }
  .poster {
    width: 740px; height: 1060px;
    background: var(--paper);
    position: relative;
    overflow: hidden;
    box-shadow: 0 2px 10px rgba(0,0,0,0.12);
  }
  .studio-line {
    position: absolute; top: 70px; left: 0; right: 0;
    text-align: center;
    font-weight: 500; font-size: 18px; line-height: 1;
    letter-spacing: 13px;
    padding-left: 13px;
  }
  .presents-line {
    position: absolute; top: 98px; left: 0; right: 0;
    text-align: center;
    font-weight: 500; font-size: 11px; line-height: 1;
    letter-spacing: 6px;
    padding-left: 6px;
    color: var(--muted);
  }
  .key-art {
    position: absolute; top: 150px; left: 50%;
    transform: translateX(-50%);
    width: 280px; height: 480px;
  }
  .tagline {
    position: absolute; top: 646px; left: 0; right: 0;
    text-align: center;
    font-weight: 500; font-size: 14px; line-height: 1;
    letter-spacing: 3px;
    color: var(--muted);
  }
  .title {
    position: absolute; top: 690px; left: 0; right: 0;
    text-align: center;
    font-weight: 700; font-size: 104px; line-height: 1;
    letter-spacing: -1px;
    transform: scaleY(1.3);
    transform-origin: top center;
  }
  .title .title-accent { color: var(--accent); }
  .billing-block {
    position: absolute; top: 842px; left: 0; right: 0;
    text-align: center;
    font-weight: 500; font-size: 14px; line-height: 20px;
    color: var(--muted);
    text-transform: uppercase;
  }
  .billing-row { white-space: nowrap; }
  .billing-label {
    display: inline-block;
    font-size: 6px; line-height: 6px;
    vertical-align: middle;
    margin: 0 3px 0 8px;
    text-align: right;
    white-space: nowrap;
  }
  .billing-row .billing-label:first-child { margin-left: 0; }
  .billing-credit { font-weight: 600; color: var(--ink); }
  .website {
    position: absolute; top: 972px; left: 0; right: 0;
    text-align: center;
    font-weight: 600; font-size: 22px; line-height: 1;
    letter-spacing: 2px;
    color: var(--ink);
  }
</style>
</head>
<body>
<main class="canvas">
  <article class="poster">
    <p class="studio-line">BRAVELLPRODUCTIONS</p>
    <p class="presents-line">PRESENTS:</p>

    <svg class="key-art" viewBox="0 0 280 480" role="img" aria-label="Photograph of an open pizza box holding the last triangular slice of a film reel, with grease-like reel marks on the lid">
      <defs>
        <linearGradient id="photoTone" x1="0" y1="0" x2="0" y2="1">
          <stop offset="0" stop-color="var(--photo-light)"/>
          <stop offset="1" stop-color="var(--photo-dark)"/>
        </linearGradient>
      </defs>
      <rect x="0" y="0" width="280" height="480" fill="url(#photoTone)"/>
    </svg>

    <p class="tagline">HURRY! THEY'RE SAVING YOU A PIECE!</p>

    <h1 class="title">COPPER<span class="title-accent">VIGIL</span></h1>

    <section class="billing-block">
      <p class="billing-row">NORTHGATE PICTURES<span class="billing-label">PRESENTS<br>A</span>PRODUCERS<span class="billing-label">A FILM<br>BY</span>SCRIPT WRITER ACTOR TWO "MOVIE TITLE"</p>
      <p class="billing-row"><span class="billing-label">MUSIC<br>BY</span>THE MUSIAN<span class="billing-label">COSTUME<br>DESIGNER</span>DESIGNER NAME<span class="billing-label">EDITED<br>BY</span>EDITORS NAME<span class="billing-label">PRODUCTION<br>DESIGNER</span>DESIGNERS NAME<span class="billing-label">DIRECTOR OF<br>PHOTOGRAPHY</span>CINEMATOGRAPHER</p>
      <p class="billing-row"><span class="billing-label">EXECUTIVE<br>PRODUCER</span>EX PRODUCER 1 EX PRODUCER 2<span class="billing-label">PRODUCED<br>BY</span>PRODUCER ONE PRODUCER 2<span class="billing-label">STORY<br>BY</span>STORY WRITER</p>
      <p class="billing-row"><span class="billing-label">SCREENPLAY<br>BY</span>SCREEN WRITER<span class="billing-label">DIRECTED<br>BY</span>DIRECTOR NAME</p>
      <p class="billing-row billing-credit">WRITTEN, PRODUCED, DIRECTED AND EDITED BY MEREDITH L. DUNBAR &amp; OWEN R. FELDMANN</p>
    </section>

    <p class="website">WWW.COPPERVIGILMOVIE.EXAMPLE</p>
  </article>
</main>
</body>
</html>
```